VaultMeridan Business Card Re-Design

VaultMeridan is a specialized information security company that applies its proven methodology of security Assessment, Development, Integration and Training (A-D-I-T) to provide cyber security services in the areas of Data Protection, Network Defense and Compliance. We need the current business card re-designed to properly scale the fonts and possibly rearranging some elements (icons, lettering, etc.) to make the card more appealing to the eye. The card should have the logo that is on the web site (www.vaultmeridan-example.com). We would like ideas for both a black card (black background) and a white card (white background). We prefer rounded corners to help the card stand out but are open to all ideas. FYI: VaultMeridan's slogan is "...your security is our business".

Target Market(s)

#1 US Government Contracting Companies, #2 Commercial Companies, #3 Gen. Public.

Industry/Entity Type

Business

Contact Information for Business Card

See Description; open to the use of different fonts.

Font styles to use
Sans Serif

Colors
000000
ec1f27
ffffff

Requirements
Must have
• Company logo on web site, rounded corners, list of company offerings on the back of the card.
Nice to have
• Icons
Should not have
• none

```html
<!DOCTYPE html>
<html lang="en">
<head>
<meta charset="utf-8">
<title>VaultMeridan Business Card</title>
<link rel="stylesheet" href="https://fonts.googleapis.com/css2?family=Open+Sans:wght@400;600;700&display=swap">
<style>
  :root {
    --ink: #000000;
    --signal: #ec1f27;
    --paper: #ffffff;
    --silver: #f4f4f4;
    --backdrop: #e9e7e4;
    --rule: #8a8a8a;
    --contact-ink: #222222;
  }
  * { box-sizing: border-box; margin: 0; padding: 0; }
  html, body {
    width: 1200px; height: 1120px; overflow: hidden;
    background: var(--backdrop);
    font-family: "Open Sans", Arial, sans-serif;
  }
  .card {
    position: absolute; left: 150px;
    width: 900px; height: 514px;
    background: var(--ink); color: var(--paper);
    border-radius: 8px; overflow: hidden;
    box-shadow: 0 10px 30px rgba(0,0,0,.25);
  }
  .card--back { top: 30px; }
  .card--front { top: 576px; }

  .brand { position: absolute; text-align: center; }
  .brand__name {
    display: flex; align-items: center; justify-content: center; gap: 12px;
    font-size: 38px; font-weight: 600; color: var(--paper); letter-spacing: 1px;
  }
  .brand__dot { width: 18px; height: 18px; border-radius: 50%; background: var(--signal); }
  .brand__tagline { margin-top: 10px; font-size: 19px; font-weight: 600; color: var(--paper); }

  .card--back .brand { left: 40px; width: 360px; top: 230px; }
  .divider { position: absolute; left: 420px; top: 50px; width: 2px; height: 380px; background: var(--rule); }
  .offerings { position: absolute; left: 450px; top: 48px; list-style: none; }
  .offerings li {
    display: flex; align-items: center; gap: 10px;
    font-size: 18.5px; line-height: 28.5px; color: var(--paper);
  }
  .offerings svg { width: 13px; height: 13px; flex: none; }
  .slogan {
    position: absolute; left: 0; right: 0; bottom: 30px; text-align: center;
    font-size: 20px; letter-spacing: 2px; color: var(--paper);
  }

  .card--front .brand { left: 40px; width: 380px; top: 150px; }
  .swoosh { position: absolute; inset: 0; width: 900px; height: 514px; }
  .holder { position: absolute; right: 40px; top: 26px; text-align: right; }
  .holder__name { font-size: 29px; font-weight: 700; }
  .holder__title { margin-top: 4px; font-size: 20px; }
  .holder__creds { color: var(--signal); }
  .holder__address { margin-top: 12px; font-size: 20px; line-height: 26px; }
  .contacts { position: absolute; right: 40px; top: 305px; list-style: none; text-align: right; }
  .contacts li {
    display: flex; align-items: center; justify-content: flex-end; gap: 9px;
    font-size: 20.5px; line-height: 29px; color: var(--contact-ink);
  }
  .contacts svg { width: 18px; height: 18px; flex: none; }
</style>
</head>
<body>

<section class="card card--back" aria-label="Card back">
  <div class="brand">
    <div class="brand__name"><span class="brand__dot"></span>VaultMeridan</div>
    <div class="brand__tagline">Information Security Solutions</div>
  </div>
  <div class="divider"></div>
  <ul class="offerings">
    <li><svg viewBox="0 0 12 12"><path d="M0 2 L12 2 L6 11 Z" fill="#ffffff"/><path d="M0 2 L6 5 L6 11 Z" fill="#ec1f27"/></svg>Secure Cloud &amp; Open Stack Solutions</li>
    <li><svg viewBox="0 0 12 12"><path d="M0 2 L12 2 L6 11 Z" fill="#ffffff"/><path d="M0 2 L6 5 L6 11 Z" fill="#ec1f27"/></svg>Network Attack Penetration &amp; Defense</li>
    <li><svg viewBox="0 0 12 12"><path d="M0 2 L12 2 L6 11 Z" fill="#ffffff"/><path d="M0 2 L6 5 L6 11 Z" fill="#ec1f27"/></svg>Red/Blue Team</li>
    <li><svg viewBox="0 0 12 12"><path d="M0 2 L12 2 L6 11 Z" fill="#ffffff"/><path d="M0 2 L6 5 L6 11 Z" fill="#ec1f27"/></svg>Data Center Consolidation</li>
    <li><svg viewBox="0 0 12 12"><path d="M0 2 L12 2 L6 11 Z" fill="#ffffff"/><path d="M0 2 L6 5 L6 11 Z" fill="#ec1f27"/></svg>Secure Virtual Computing</li>
    <li><svg viewBox="0 0 12 12"><path d="M0 2 L12 2 L6 11 Z" fill="#ffffff"/><path d="M0 2 L6 5 L6 11 Z" fill="#ec1f27"/></svg>Classified Cross Domain Solutions</li>
    <li><svg viewBox="0 0 12 12"><path d="M0 2 L12 2 L6 11 Z" fill="#ffffff"/><path d="M0 2 L6 5 L6 11 Z" fill="#ec1f27"/></svg>Foreign/Counter Intelligence Data Security</li>
    <li><svg viewBox="0 0 12 12"><path d="M0 2 L12 2 L6 11 Z" fill="#ffffff"/><path d="M0 2 L6 5 L6 11 Z" fill="#ec1f27"/></svg>Certification &amp; Accreditation</li>
    <li><svg viewBox="0 0 12 12"><path d="M0 2 L12 2 L6 11 Z" fill="#ffffff"/><path d="M0 2 L6 5 L6 11 Z" fill="#ec1f27"/></svg>Secure Wireless Solutions</li>
    <li><svg viewBox="0 0 12 12"><path d="M0 2 L12 2 L6 11 Z" fill="#ffffff"/><path d="M0 2 L6 5 L6 11 Z" fill="#ec1f27"/></svg>Security Training, Assessment &amp; Integration</li>
    <li><svg viewBox="0 0 12 12"><path d="M0 2 L12 2 L6 11 Z" fill="#ffffff"/><path d="M0 2 L6 5 L6 11 Z" fill="#ec1f27"/></svg>Security Subject Matter Experts</li>
    <li><svg viewBox="0 0 12 12"><path d="M0 2 L12 2 L6 11 Z" fill="#ffffff"/><path d="M0 2 L6 5 L6 11 Z" fill="#ec1f27"/></svg>Executive Security Strategy Coaching</li>
    <li><svg viewBox="0 0 12 12"><path d="M0 2 L12 2 L6 11 Z" fill="#ffffff"/><path d="M0 2 L6 5 L6 11 Z" fill="#ec1f27"/></svg>Data Encryption/Privacy</li>
  </ul>
  <p class="slogan">YOUR SECURITY IS OUR BUSINESS</p>
</section>

<section class="card card--front" aria-label="Card front">
  <svg class="swoosh" viewBox="0 0 900 514" aria-hidden="true">
    <defs>
      <linearGradient id="silverFade" x1="0" y1="0" x2="1" y2="1">
        <stop offset="0" stop-color="#ffffff"/>
        <stop offset="1" stop-color="#cfcfcf"/>
      </linearGradient>
    </defs>
    <path class="swoosh__band-outer" d="M0 430 C200 440 330 400 450 330 C560 265 700 215 900 205 L900 514 L0 514 Z" fill="#ec1f27"/>
    <path class="swoosh__gap" d="M0 450 C200 455 330 420 455 345 C560 282 700 232 900 222 L900 514 L0 514 Z" fill="#000000"/>
    <path class="swoosh__band-inner" d="M0 466 C200 468 330 438 458 358 C560 296 700 244 900 233 L900 514 L0 514 Z" fill="#ec1f27"/>
    <path class="swoosh__edge" d="M0 484 C200 482 330 452 460 372 C560 310 700 256 900 246 L900 514 L0 514 Z" fill="#000000"/>
    <path class="swoosh__panel" d="M0 495 C200 490 330 460 462 382 C560 320 700 266 900 256 L900 514 L0 514 Z" fill="url(#silverFade)"/>
  </svg>

  <div class="brand">
    <div class="brand__name"><span class="brand__dot"></span>VaultMeridan</div>
    <div class="brand__tagline">Information Security Solutions</div>
  </div>

  <div class="holder">
    <div class="holder__name">Dorian Hale</div>
    <div class="holder__title">President - CEO, <span class="holder__creds">CISSP, CEH</span></div>
    <div class="holder__address">VaultMeridan, Inc.<br>4127 Brookmere Ave. Suite 210<br>Linwood, Maryland 21099</div>
  </div>

  <ul class="contacts">
    <li><svg viewBox="0 0 18 18"><circle cx="9" cy="9" r="8" fill="#ec1f27"/><path d="M6 5 L8 5 L8.5 7.5 L7.4 8.3 C8 9.6 8.7 10.3 10 10.9 L10.8 9.8 L13 10.3 L13 12.3 C9 12.5 5.6 9 6 5 Z" fill="#ffffff"/></svg>555-014-2290</li>
    <li><svg viewBox="0 0 18 18"><rect x="5" y="1" width="9" height="16" rx="2" fill="#ec1f27"/><rect x="6.5" y="3" width="6" height="8" fill="#ffffff"/><circle cx="9.5" cy="14" r="1.2" fill="#ffffff"/></svg>555-017-3384</li>
    <li><svg viewBox="0 0 18 18"><rect x="1" y="4" width="16" height="11" rx="1.5" fill="#ec1f27"/><path d="M1.5 5 L9 10.5 L16.5 5" stroke="#ffffff" stroke-width="1.4" fill="none"/></svg>info@vaultmeridan-example.com</li>
    <li><svg viewBox="0 0 18 18"><rect x="1" y="4" width="16" height="11" rx="1.5" fill="#ec1f27"/><path d="M1.5 5 L9 10.5 L16.5 5" stroke="#ffffff" stroke-width="1.4" fill="none"/></svg>dhale@vaultmeridan-example.com</li>
    <li><svg viewBox="0 0 18 18"><circle cx="9" cy="9" r="7.5" fill="none" stroke="#ec1f27" stroke-width="1.6"/><ellipse cx="9" cy="9" rx="3.2" ry="7.5" fill="none" stroke="#ec1f27" stroke-width="1.3"/><path d="M1.5 9 H16.5 M3 5 H15 M3 13 H15" stroke="#ec1f27" stroke-width="1.2"/></svg>www.vaultmeridan-example.com</li>
  </ul>
</section>

</body>
</html>
```